Design Business Cards for VAE

I am looking for business cards for my new existing consultancy/events business. It is important the business cards are fun and exciting, yet elegant.

What we do:-

Promoting Gaming Culture in India

- Manage Professional Gaming Team
- Promotional Marketing
- LAN Center Events
- Retail Events
- Tradeshow Engagement Activities
- Online Events
- Contests
- Online Community Development
- Strategy Consulting

I have attached the logo in AI format.

On the business card we would like:

- Person name
- Logo
- Title
- Website
- Email
- Phone

Most importantly, we are looking for something funky, cool and different!

```html
<!DOCTYPE html>
<html lang="en">
<head>
<meta charset="utf-8">
<title>Vertex Arena Business Cards</title>
<link href="https://fonts.googleapis.com/css2?family=Open+Sans:ital,wght@0,300;0,400;0,600;1,400&display=swap" rel="stylesheet">
<style>
  :root {
    --stage: #e6e4e1;
    --ink: #111111;
    --paper: #ffffff;
    --text-dark: #2a2a2a;
    --text-mid: #555555;
    --ghost: #efefef;
    --rule-light: #7a7a7a;
    --rule-dark: #d0d0d0;
  }
  * { margin: 0; padding: 0; box-sizing: border-box; }
  html, body {
    width: 1200px; height: 872px; overflow: hidden;
    background: var(--stage);
    font-family: "Open Sans", Arial, sans-serif;
  }
  .canvas { position: relative; width: 1200px; height: 872px; }

  /* Front card */
  .card-front {
    position: absolute; left: 130px; top: 190px;
    width: 320px; height: 500px;
    background: var(--ink); color: var(--paper);
    box-shadow: 0 10px 30px rgba(0,0,0,.25);
  }
  .front-mark {
    position: absolute; left: 50%; top: 96px; transform: translateX(-50%);
    display: flex; align-items: center; gap: 10px;
  }
  .front-mark .mark-square { width: 12px; height: 12px; background: var(--paper); }
  .front-mark .mark-name { font-weight: 600; font-size: 56px; letter-spacing: 4px; line-height: 1; }
  .front-rule {
    position: absolute; left: 60px; right: 60px; top: 200px;
    height: 1px; background: var(--rule-light);
  }
  .front-tagline {
    position: absolute; left: 246px; top: 214px;
    transform-origin: 0 0; transform: rotate(90deg);
    font-weight: 400; font-size: 22px; line-height: 1.05;
    text-transform: uppercase; letter-spacing: .5px; white-space: nowrap;
  }
  .front-tagline .accent { font-weight: 600; }

  /* Back card */
  .card-back {
    position: absolute; left: 520px; top: 250px;
    width: 560px; height: 330px;
    background: var(--paper); color: var(--text-dark);
    box-shadow: 0 10px 30px rgba(0,0,0,.2);
    overflow: hidden;
  }
  .corner { position: absolute; width: 0; height: 0; }
  .corner-left { left: 0; top: 70px; border-top: 14px solid transparent; border-bottom: 14px solid transparent; border-left: 14px solid var(--ink); }
  .corner-right { right: 0; top: 270px; border-top: 14px solid transparent; border-bottom: 14px solid transparent; border-right: 14px solid var(--ink); }

  .ghost-name {
    position: absolute; left: 50%; top: 52%; transform: translate(-50%,-50%);
    font-weight: 600; font-size: 140px; color: var(--ghost); letter-spacing: 6px;
  }
  .holder { position: absolute; left: 34px; top: 28px; }
  .holder-name { display: flex; align-items: center; gap: 8px; font-size: 19px; font-weight: 600; }
  .holder-title { margin-left: 22px; font-size: 11px; color: var(--text-mid); }

  .service-list { list-style: none; font-style: italic; font-size: 12px; line-height: 1.6; color: var(--text-dark); }
  .service-list.primary { position: absolute; left: 34px; top: 96px; }
  .service-list.secondary { position: absolute; left: 300px; top: 200px; }

  .contact { position: absolute; left: 300px; top: 96px; list-style: none; font-size: 12px; color: var(--text-dark); }
  .contact li { display: flex; align-items: center; gap: 8px; margin-bottom: 7px; }
  .contact-rule { position: absolute; left: 290px; top: 96px; width: 1px; height: 66px; background: var(--rule-dark); }
</style>
</head>
<body>
<main class="canvas">

  <section class="card-front" aria-label="Card front">
    <div class="front-mark">
      <span class="mark-square"></span>
      <span class="mark-name">VAE</span>
    </div>
    <div class="front-rule"></div>
    <p class="front-tagline">Vertex<br><span class="accent">Arena</span><br>Entertainment</p>
  </section>

  <section class="card-back" aria-label="Card back">
    <span class="corner corner-left"></span>
    <span class="corner corner-right"></span>
    <div class="ghost-name" aria-hidden="true">VAE</div>

    <div class="holder">
      <div class="holder-name">
        <svg width="14" height="14" viewBox="0 0 14 14" aria-hidden="true"><circle cx="7" cy="4" r="3" fill="#2a2a2a"/><path d="M1 14c0-4 3-6 6-6s6 2 6 6z" fill="#2a2a2a"/></svg>
        Marcus Hale
      </div>
      <div class="holder-title">Director</div>
    </div>

    <ul class="service-list primary">
      <li>Promoting Gaming Culture in India</li>
      <li>-Manage Professional Gaming Team</li>
      <li>-Promotional Marketing</li>
      <li>-LAN Center Events</li>
      <li>-Contests</li>
    </ul>

    <span class="contact-rule"></span>
    <ul class="contact">
      <li>
        <svg width="14" height="14" viewBox="0 0 14 14" aria-hidden="true"><circle cx="7" cy="7" r="7" fill="#2a2a2a"/><path d="M4.5 3.5l1.5 0 .6 1.8-.9.7a5 5 0 0 0 2.3 2.3l.7-.9 1.8.6v1.5c-3.5.3-6.3-2.5-6-6z" fill="#fff"/></svg>
        07 555 010 234
      </li>
      <li>
        <svg width="14" height="14" viewBox="0 0 14 14" aria-hidden="true"><circle cx="7" cy="7" r="7" fill="#2a2a2a"/><rect x="3.5" y="4.5" width="7" height="5" fill="none" stroke="#fff" stroke-width="1"/><path d="M3.5 4.5l3.5 3 3.5-3" fill="none" stroke="#fff" stroke-width="1"/></svg>
        hello@vertexarena.com
      </li>
      <li>
        <svg width="14" height="14" viewBox="0 0 14 14" aria-hidden="true"><circle cx="7" cy="7" r="7" fill="#2a2a2a"/><circle cx="7" cy="7" r="3.6" fill="none" stroke="#fff" stroke-width="1"/><path d="M3.4 7h7.2M7 3.4c-1.6 2-1.6 5.2 0 7.2M7 3.4c1.6 2 1.6 5.2 0 7.2" fill="none" stroke="#fff" stroke-width=".8"/></svg>
        www.vertexarena.com
      </li>
    </ul>

    <ul class="service-list secondary">
      <li>-Retail Events</li>
      <li>-Tradeshow Engagement Activities</li>
      <li>-Online Events</li>
      <li>-Online Community Development</li>
      <li>-Strategy Consulting</li>
    </ul>
  </section>

</main>
</body>
</html>
```